Security Camera Sign

14” high x 11” wide Color: Blue, Yellow, Black and white

Make the sign vertical
Replace red with blue
WARNING: Black over yellow
These premises are protected by Closed Circuit Television: On white
Images are recorded for crime prevention and public safety. Unauthorized access, theft or vandalism will result in prosecution: On Blue

Target Market(s)

Outdoor commercial building

Industry/Entity Type

Security

Requirements
Nice to have
• I would like the sign stand out. If you need more colors? Thanks Ok

```html
<!DOCTYPE html>
<html lang="en">
<head>
<meta charset="utf-8">
<title>Surveillance Sign</title>
<link href="https://fonts.googleapis.com/css2?family=Open+Sans:ital,wght@0,700;1,400&family=Orbitron:wght@900&display=swap" rel="stylesheet">
<style>
  :root {
    --sign-blue: #30318f;
    --sign-yellow: #ffe20f;
    --ink: #000000;
    --paper: #ffffff;
  }
  html, body {
    margin: 0;
    padding: 0;
    overflow: hidden;
    background: var(--paper);
  }
  .sign {
    position: relative;
    width: 943px;
    height: 1200px;
    background: var(--paper);
    overflow: hidden;
  }
  .header-band {
    position: absolute;
    left: 0; top: 0;
    width: 943px;
    height: 214px;
    background: var(--sign-blue);
  }
  .title-plate {
    position: absolute;
    left: 52px; top: 36px;
    width: 832px;
    height: 135px;
    background: var(--sign-yellow);
    border: 3px solid var(--ink);
    border-radius: 10px;
    display: flex;
    align-items: center;
    justify-content: center;
  }
  .title-plate h1 {
    margin: 0;
    font-family: "Open Sans", sans-serif;
    font-weight: 700;
    font-size: 104px;
    line-height: 1;
    letter-spacing: -1px;
    color: var(--ink);
  }
  .camera-art {
    position: absolute;
    left: 401px; top: 237px;
    width: 533px;
    height: 320px;
    background: linear-gradient(160deg, #1a1a1a, #000000);
    border-radius: 12px;
  }
  .notice {
    position: absolute;
    left: 36px; top: 0;
    margin: 0;
    font-family: "Orbitron", sans-serif;
    font-weight: 900;
    font-style: italic;
    font-size: 55px;
    color: var(--ink);
  }
  .notice-line {
    position: absolute;
    left: 0;
    white-space: nowrap;
    line-height: 1;
  }
  .footer-band {
    position: absolute;
    left: 0; top: 985px;
    width: 943px;
    height: 215px;
    background: var(--sign-blue);
    display: flex;
    align-items: center;
    justify-content: center;
  }
  .footer-band p {
    margin: 0;
    font-family: "Open Sans", sans-serif;
    font-style: italic;
    font-weight: 400;
    font-size: 35px;
    line-height: 55px;
    text-align: center;
    color: var(--paper);
  }
</style>
</head>
<body>
<main class="sign">
  <header class="header-band">
    <div class="title-plate"><h1>SURVEILLANCE</h1></div>
  </header>

  <div class="camera-art" role="img" aria-label="Black illustration of a wall-mounted CCTV security camera"></div>

  <h2 class="notice">
    <span class="notice-line" style="top:482px">THESE</span>
    <span class="notice-line" style="top:583px">PREMISES ARE</span>
    <span class="notice-line" style="top:684px">PROTECTED BY</span>
    <span class="notice-line" style="top:786px">CLOSED</span>
    <span class="notice-line" style="top:888px">CIRCUIT TELEVISION</span>
  </h2>

  <footer class="footer-band">
    <p>Images are recorded for crime prevention and<br>public safety. Unauthorized access, theft or<br>vandalism will result in prosecution</p>
  </footer>
</main>
</body>
</html>
```